M Zyvantics Buisness Cards

I need a technology focused clean business card for my employees. I have attached out logo to include in the mocks. We're a modern tech consulting firm that drives to interface humanity with technology in a truly cohesive fashion.

```html
<!DOCTYPE html>
<html lang="en">
<head>
<meta charset="utf-8">
<title>M Zyvantics Business Cards</title>
<link href="https://fonts.googleapis.com/css2?family=Arimo:wght@400;700&display=swap" rel="stylesheet">
<style>
  :root {
    --stage: #2b2b2d;
    --card-blue: #1b78c6;
    --card-blue-deep: #1568b0;
    --card-dark: #313234;
    --ink-white: #ffffff;
    --ink-grey: #8c8e92;
    --ink-light: #e4e5e7;
    --accent: #1f7ad0;
  }
  * { box-sizing: border-box; margin: 0; padding: 0; }
  html, body {
    width: 1200px; height: 997px; overflow: hidden;
    background: var(--stage);
    font-family: "Arimo", Arial, sans-serif;
  }
  .stage { position: relative; width: 1200px; height: 997px; }
  .card {
    position: absolute; width: 560px; height: 320px; border-radius: 18px;
    box-shadow: 0 18px 40px rgba(0,0,0,.45);
  }
  .card--front {
    left: 60px; top: 130px;
    background: linear-gradient(135deg, var(--card-blue) 0%, var(--card-blue-deep) 100%);
    display: flex; align-items: center; justify-content: center;
  }
  .card--back { left: 580px; top: 500px; background: var(--card-dark); }
  .brand { display: flex; align-items: center; gap: 16px; }
  .brand__dot { width: 34px; height: 34px; border-radius: 50%; }
  .brand__name { font-weight: 700; font-size: 44px; letter-spacing: 1px; }
  .card--front .brand__dot { background: var(--ink-white); }
  .card--front .brand__name { color: var(--ink-white); }
  .card--back .brand { position: absolute; left: 36px; top: 136px; gap: 12px; }
  .card--back .brand__dot { width: 26px; height: 26px; background: var(--accent); }
  .card--back .brand__name { font-size: 30px; color: var(--ink-grey); }
  .divider {
    position: absolute; left: 296px; top: 70px; width: 2px; height: 180px;
    background: linear-gradient(to bottom, transparent, var(--accent) 30%, var(--accent) 70%, transparent);
  }
  .contact { position: absolute; left: 322px; top: 78px; color: var(--ink-light); font-size: 13px; line-height: 1.35; }
  .contact__name { color: var(--accent); font-weight: 700; font-size: 17px; letter-spacing: .5px; }
  .contact__role { margin-bottom: 14px; }
  .contact__address { margin-bottom: 10px; }
  .contact__line { display: flex; align-items: center; gap: 8px; margin-bottom: 4px; }
  .contact__line svg { width: 11px; height: 11px; fill: var(--accent); }
  .contact__web { color: var(--accent); font-weight: 700; letter-spacing: 1px; margin-left: 19px; }
</style>
</head>
<body>
<main class="stage">
  <section class="card card--front" aria-label="Card front">
    <div class="brand">
      <span class="brand__dot"></span>
      <span class="brand__name">M Zyvantics</span>
    </div>
  </section>

  <section class="card card--back" aria-label="Card back">
    <div class="brand">
      <span class="brand__dot"></span>
      <span class="brand__name">M Zyvantics</span>
    </div>
    <div class="divider"></div>
    <div class="contact">
      <p class="contact__name">DANIEL MARSH</p>
      <p class="contact__role">Director</p>
      <p class="contact__address">P.O. Box KL318, Harbourview<br>HV KL, Coralia</p>
      <p class="contact__line">
        <svg viewBox="0 0 24 24" aria-hidden="true"><path d="M6.6 10.8a15.1 15.1 0 0 0 6.6 6.6l2.2-2.2a1 1 0 0 1 1-.25 11.4 11.4 0 0 0 3.6.57 1 1 0 0 1 1 1V20a1 1 0 0 1-1 1A17 17 0 0 1 3 4a1 1 0 0 1 1-1h3.5a1 1 0 0 1 1 1c0 1.25.2 2.45.57 3.57a1 1 0 0 1-.25 1z"/></svg>
        1441 555 0147
      </p>
      <p class="contact__line">
        <svg viewBox="0 0 24 24" aria-hidden="true"><path d="M2 5h20v14H2z M2 5l10 8 10-8" /></svg>
        dmarsh@zyvantics.com
      </p>
      <p class="contact__web">www.zyvantics.com</p>
    </div>
  </section>
</main>
</body>
</html>
```